Business Card Design

Copperfield Lantern Works, Inc. (CLW), located in Memphis, TN began operating on 2003. We are a certified
minority woman-owned business that genuinely takes a vested interest in our customers. We serve utilities,
government, contractors and end user markets in electrical, water, gas and industrial supplies. Our core
competency as a distributor of electrical materials has positioned us to serve business of all size. As your supply
chain partner, we arm you with the resources you need to make your supply chain more efficient. Our team
works with your team on a daily basis to help you solve problems and achieve goals. This team approach has
helped CLW customers to succeed and we can do the same for you.

NAICS Codes:
423610 Electrical Apparatus and Equipment, Wiring Supplies, and Related Equipment Merchant
Wholesalers
423510 Metal Service Centers and Other Metal Merchant Wholesalers
423720 Plumbing and Heating Equipment and Supplies (Hydronics) Merchant Wholesalers

Certifications
MBE (KRVPQAL, Valdren State Up-RFX and HJW), WBE (QOZRT),
WOSB, DOT (KXPT, MQRT, ZLVRT, SQWRT, NJWRT, and VPXT), LOSB,
SBE, and LSB Certified
Some of Our Products Include:
. Boxes & Covers
. Conduit & Raceway
. Fittings
. Fuses
. Lamp & Ballasts
. Lighting Controls & Timers
. Lighting Fixtures
. Personal Safety
. Pipes
. Power Distribution
. Terminations Ground & Splices
. Tools & Testers
. Wire, Cords & Cable
. Wiring Devices
. Valves

Industry/Entity Type

Business

Contact Information for Business Card

Harriet M. Pendlow - President/CEO
4817 Galvin Ave., Memphis, TN 38127
901-482-6317 office, 901-482-6319 fax, 901-358-2074 cell
hmpendlow@clwgroupx.com - www.clwworksx.com

```html
<!DOCTYPE html>
<html lang="en">
<head>
<meta charset="utf-8">
<title>Copperfield Lantern Works – Business Card</title>
<link rel="stylesheet" href="https://fonts.googleapis.com/css2?family=Source+Sans+3:wght@400;600&display=swap">
<style>
  :root {
    --ink: #0c0c0c;
    --paper: #f5f5f2;
    --olive: #8c9a52;
    --olive-dark: #6f7c3c;
    --stage: #e8e5df;
    --muted: #d9d9d4;
  }
  * { box-sizing: border-box; margin: 0; padding: 0; }
  html, body { width: 1200px; height: 780px; overflow: hidden; }
  body {
    background: var(--stage);
    font-family: "Source Sans 3", "Helvetica Neue", Arial, sans-serif;
    position: relative;
  }
  .card {
    position: absolute;
    top: 230px;
    width: 560px;
    height: 320px;
    overflow: hidden;
    box-shadow: 0 4px 14px rgba(0,0,0,.18);
  }
  .card--front { left: 30px; background: var(--paper); }
  .card--back { left: 610px; background: var(--ink); }
  .card__shapes { position: absolute; inset: 0; }

  .wordmark { position: absolute; display: flex; align-items: center; gap: 10px; }
  .wordmark__mark { width: 14px; height: 14px; background: var(--olive); flex: none; }
  .wordmark__name {
    font-weight: 600;
    font-size: 24px;
    line-height: 1.02;
    letter-spacing: .5px;
    text-transform: uppercase;
  }
  .card--front .wordmark { left: 34px; top: 86px; }
  .card--front .wordmark__name { color: var(--ink); }
  .card--back .wordmark { left: 232px; top: 34px; }
  .card--back .wordmark__name { color: var(--paper); font-size: 26px; }

  .contact { position: absolute; right: 26px; top: 22px; text-align: right; color: var(--ink); }
  .contact__name { font-size: 20px; font-weight: 600; }
  .contact__title { font-size: 14px; color: var(--olive); margin-bottom: 10px; }
  .contact__line {
    display: flex; justify-content: flex-end; align-items: center; gap: 6px;
    font-size: 13px; line-height: 17px;
  }
  .contact__icon { width: 11px; height: 11px; background: var(--olive); flex: none; }

  .social { position: absolute; right: 22px; bottom: 48px; display: flex; gap: 7px; }
  .social__badge { width: 20px; height: 20px; border-radius: 3px; background: var(--muted); }

  .certs { position: absolute; left: 22px; top: 206px; width: 330px; color: var(--paper); }
  .certs__heading { font-size: 19px; color: var(--olive); font-weight: 600; margin-bottom: 2px; }
  .certs__text { font-size: 11.5px; line-height: 14px; }

  .strip-text {
    position: absolute; left: 44px; bottom: 8px;
    font-size: 13px; color: var(--paper); letter-spacing: .3px;
  }

  .products { position: absolute; left: 36px; top: 122px; color: var(--paper); }
  .products__heading { font-size: 19px; color: var(--olive); font-weight: 600; margin: 0 0 6px 170px; }
  .products__line { font-size: 12.5px; line-height: 18px; }
  .address {
    position: absolute; left: 40px; bottom: 8px;
    font-size: 13px; color: var(--paper); letter-spacing: .3px;
  }
</style>
</head>
<body>

  <section class="card card--front" aria-label="Business card front">
    <svg class="card__shapes" width="560" height="320" viewBox="0 0 560 320" aria-hidden="true">
      <polygon points="0,206 236,206 282,140 330,188 560,188 560,320 0,320" fill="var(--ink)"/>
      <polyline points="0,197 230,197 277,128 331,178 560,178" fill="none" stroke="var(--olive)" stroke-width="12"/>
      <polygon points="0,290 300,290 286,320 0,320" fill="var(--olive)"/>
    </svg>

    <div class="wordmark">
      <span class="wordmark__mark"></span>
      <span class="wordmark__name">Copperfield<br>Lantern Works</span>
    </div>

    <div class="contact">
      <div class="contact__name">Harriet M. Pendlow</div>
      <div class="contact__title">President/CEO</div>
      <div class="contact__line">901-482-6317 <span class="contact__icon"></span></div>
      <div class="contact__line">901-358-2074 <span class="contact__icon"></span></div>
      <div class="contact__line">901-482-6319 <span class="contact__icon"></span></div>
      <div class="contact__line">hmpendlow@clwgroupx.com <span class="contact__icon"></span></div>
    </div>

    <div class="social">
      <span class="social__badge"></span>
      <span class="social__badge"></span>
      <span class="social__badge"></span>
      <span class="social__badge"></span>
    </div>

    <div class="certs">
      <div class="certs__heading">Certifications</div>
      <p class="certs__text">MBE (KRVPQAL, Valdren State Up-RFX and HJW),
        WBE(QOZRT),WOSB,DOT (KXPT,MQRT,ZLVRT,SQWRT,
        NJWRT,and VPXT),LOSB,SBE,and LSB Certified</p>
    </div>

    <div class="strip-text">www.clwworksx.com</div>
  </section>

  <section class="card card--back" aria-label="Business card back">
    <svg class="card__shapes" width="560" height="320" viewBox="0 0 560 320" aria-hidden="true">
      <polygon points="0,286 380,286 362,320 0,320" fill="var(--olive)"/>
      <line x1="0" y1="286" x2="380" y2="286" stroke="var(--olive-dark)" stroke-width="2"/>
    </svg>

    <div class="wordmark">
      <span class="wordmark__mark"></span>
      <span class="wordmark__name">Copperfield<br>Lantern Works</span>
    </div>

    <div class="products">
      <div class="products__heading">Our Products Include</div>
      <p class="products__line">Boxes &amp; Covers | Conduit &amp; Raceway | Fittings | Fuses | Lamp &amp; Ballasts</p>
      <p class="products__line">Lighting Controls &amp; Timers | Lighting Fixtures | Personal Safety | Pipes</p>
      <p class="products__line">Power Distribution | Terminations Ground &amp; Splices | Tools &amp; Testers</p>
      <p class="products__line">Wire Cords &amp; Cable | Wiring Devices | Valves</p>
    </div>

    <div class="address">4817 Galvin Ave, Memphis, TN 38127</div>
  </section>

</body>
</html>
```